Silverleaf Rise Accounting Program

size of ad Full: 7” x 9.6”
1- this is for a ladies program so it should appeal to women.
2-however, I do not want any pictures of people in this ad.
3-all the text should be seen and not covered over by graphics.
4-It should be an ad that will draw people's attention and people should look at it and say it looks nice I want to see that ad.
5-I have put all the instructions in yellow in the file below.
6-please leave 1 inch for the footer .
good luck with this project

• no picture or vector of people.

```html
<!DOCTYPE html>
<html lang="en">
<head>
<meta charset="utf-8">
<title>Silverleaf Rise Accounting Program</title>
<link rel="stylesheet" href="https://fonts.googleapis.com/css2?family=League+Spartan:wght@700;800;900&family=Catamaran:wght@500;700;800&family=Roboto:wght@400;500&display=swap">
<style>
  :root {
    --ink: #0b0b0b;
    --paper: #f7f7f7;
    --gold: #f2c037;
    --gold-deep: #e9a81c;
    --white: #ffffff;
  }
  * { margin: 0; padding: 0; box-sizing: border-box; }
  html, body { width: 893px; height: 1200px; overflow: hidden; background: var(--paper); }
  .ad { position: relative; width: 893px; height: 1200px; background: var(--paper); color: var(--ink); font-family: "Catamaran", sans-serif; }
  .abs { position: absolute; }

  .headline { left: 0; width: 893px; text-align: center; font-family: "League Spartan", sans-serif; font-weight: 800; line-height: 1; letter-spacing: 1px; }
  .headline--one { top: 70px; font-size: 126px; }
  .headline--two { top: 183px; font-size: 126px; }

  .rule { left: 19px; width: 855px; border-top: 2px dashed #333; }
  .rule--top { top: 297px; }
  .rule--bottom { top: 359px; }

  .degree { top: 306px; left: 0; width: 893px; text-align: center; font-weight: 800; font-size: 43px; letter-spacing: 1.5px; line-height: 1.1; }
  .pitch { top: 370px; left: 0; width: 893px; text-align: center; font-weight: 500; font-size: 25px; line-height: 33px; }

  .advantage-band { top: 451px; left: 0; width: 893px; height: 66px; background: var(--gold); text-align: center; font-weight: 800; font-size: 42px; line-height: 72px; }

  .stat-box { border: 2px dashed #333; }
  .stat-rate { left: 45px; top: 554px; width: 326px; height: 247px; }
  .stat-rate__bar { left: 45px; top: 791px; width: 326px; height: 10px; background: var(--gold); }
  .big-number { font-family: "League Spartan", sans-serif; font-weight: 900; color: var(--ink); line-height: 1; text-shadow: 4px -3px 0 var(--gold); }
  .stat-rate .big-number { position: absolute; left: 20px; top: 12px; font-size: 128px; letter-spacing: -2px; }
  .stat-rate__label { position: absolute; left: 0; top: 132px; width: 100%; text-align: center; font-family: "Roboto", sans-serif; font-weight: 500; font-size: 46px; line-height: 48px; }

  .stat-directors { left: 388px; top: 554px; width: 460px; height: 117px; }
  .stat-directors__bar { left: 388px; top: 554px; width: 12px; height: 117px; background: var(--gold); }
  .stat-directors .big-number { position: absolute; left: 40px; top: 8px; font-size: 118px; }
  .stat-directors__label { position: absolute; left: 152px; top: 10px; font-family: "Roboto", sans-serif; font-weight: 500; font-size: 45px; line-height: 51px; }

  .stat-firms { left: 388px; top: 685px; width: 460px; height: 116px; }
  .stat-firms__bar { left: 836px; top: 685px; width: 12px; height: 116px; background: var(--gold); }
  .stat-firms__lead { position: absolute; left: 14px; top: 10px; font-family: "Roboto", sans-serif; font-size: 28px; }
  .stat-firms__main { position: absolute; left: 12px; top: 46px; font-family: "Catamaran", sans-serif; font-weight: 800; font-size: 58px; line-height: 1.1; letter-spacing: 1px; }

  .event-band { top: 833px; left: 0; width: 893px; height: 73px; background: var(--ink); color: var(--white); }
  .event-band__title { position: absolute; left: 65px; top: 10px; color: var(--gold); font-weight: 700; font-size: 27px; letter-spacing: 0.5px; line-height: 30px; }
  .event-band__date { position: absolute; left: 65px; top: 42px; font-family: "Roboto", sans-serif; font-size: 22px; }
  .event-band__divider { position: absolute; left: 375px; top: 14px; width: 2px; height: 48px; background: var(--gold); }
  .event-band__info { position: absolute; left: 401px; top: 11px; font-family: "Roboto", sans-serif; font-size: 18px; line-height: 28px; }

  .ranking-badge { left: 50px; top: 930px; }
  .school { left: 158px; top: 950px; }
  .school__name { font-weight: 800; font-size: 32px; line-height: 1.2; }
  .school__note { font-family: "Roboto", sans-serif; font-size: 22px; line-height: 28px; }

  .seal { left: 694px; top: 913px; width: 160px; height: 160px; }
  .seal__text { position: absolute; left: 0; top: 26px; width: 100%; text-align: center; font-family: "Roboto", sans-serif; color: var(--ink); }
  .seal__small { font-size: 17px; font-weight: 500; display: block; }
  .seal__big { font-family: "League Spartan", sans-serif; font-weight: 900; font-size: 66px; line-height: 62px; display: block; }
  .seal__months { font-size: 21px; display: block; line-height: 18px; }

  .footer { left: 0; top: 1076px; width: 893px; height: 124px; background: var(--ink); }
</style>
</head>
<body>
<main class="ad">
  <h1 class="abs headline headline--one">ATTENTION</h1>
  <div class="abs headline headline--two">WOMEN!</div>

  <div class="abs rule rule--top"></div>
  <h2 class="abs degree">A Master’s Degree in Accounting</h2>
  <div class="abs rule rule--bottom"></div>
  <p class="abs pitch">A stable, lucrative career, with high-paying, full /part time<br>opportunities in Private/Public companies</p>

  <div class="abs advantage-band">The Meridian Job Placement advantage</div>

  <section class="abs stat-box stat-rate">
    <div class="big-number">96%</div>
    <div class="stat-rate__label">PLACEMENT<br>RATE</div>
  </section>
  <div class="abs stat-rate__bar"></div>

  <section class="abs stat-box stat-directors">
    <div class="big-number">6</div>
    <div class="stat-directors__label">PLACEMENT<br>DIRECTORS</div>
  </section>
  <div class="abs stat-directors__bar"></div>

  <section class="abs stat-box stat-firms">
    <div class="stat-firms__lead">Decades Of Relationships With</div>
    <div class="stat-firms__main">100’s Of Firms</div>
  </section>
  <div class="abs stat-firms__bar"></div>

  <section class="abs event-band">
    <div class="event-band__title">VIDLINK OPEN HOUSE</div>
    <div class="event-band__date">Sunday June 14, 2:00 pm</div>
    <div class="event-band__divider"></div>
    <div class="event-band__info">For A Vidlink Link / Conference Number /information<br>info@meridianjobs.org&nbsp; Or 555 014 2800x111</div>
  </section>

  <svg class="abs ranking-badge" width="92" height="92" viewBox="0 0 92 92" role="img" aria-label="Program ranking badge">
    <circle cx="46" cy="46" r="42" fill="var(--gold-deep)"/>
  </svg>

  <div class="abs school">
    <div class="school__name">Harrowgate Crest University,</div>
    <div class="school__note">Masters in Accounting program,<br>Received the highest possible rating in USA</div>
  </div>

  <div class="abs seal">
    <svg width="160" height="160" viewBox="0 0 160 160" aria-hidden="true">
      <circle cx="80" cy="80" r="76" fill="var(--gold)"/>
    </svg>
    <div class="seal__text">
      <span class="seal__small">Masters in</span>
      <span class="seal__big">12</span>
      <span class="seal__months">months</span>
    </div>
  </div>

  <footer class="abs footer"></footer>
</main>
</body>
</html>
```